VORNAK (PTY)LTD Website design

WEBSITE design based on our different divisions in our organization.
Our company specializes in the following.
Construction
Property development
Demolition
Mining
Transport
Manufacturing of concrete bricks and blocks
Lightweight concrete Readymix
I want a very modern website and look that fits in with our organization and the changing times of the world.
The website must be very professional and crisp and should appeal to both the younger generation and older generation of business leaders and.
The website must be very user friendly and easy to navigate, simple yet modern, professional and corporate.

```html
<!DOCTYPE html>
<html lang="en">
<head>
<meta charset="utf-8">
<title>VORNAK (PTY)LTD</title>
<link href="https://fonts.googleapis.com/css2?family=Montserrat:wght@400;500;600;700;800&display=swap" rel="stylesheet">
<style>
:root{
  --blue:#1a6cbd;
  --sky:#27a2e0;
  --ink:#222;
  --text:#444;
  --grey-bg:#f2f2f2;
  --white:#fff;
}
*{box-sizing:border-box;margin:0;padding:0}
html,body{width:1200px;height:3943px;overflow:hidden}
body{position:relative;font-family:'Montserrat',sans-serif;color:var(--text);background:var(--white)}
.abs{position:absolute}
a{color:inherit;text-decoration:none}

/* header */
.site-header{left:0;top:0;width:1200px;height:120px;background:var(--white)}
.brand{left:111px;top:30px}
.brand-name{font-size:46px;font-weight:700;color:var(--blue);line-height:1;letter-spacing:1px}
.top-contact{right:112px;top:20px;display:flex;gap:16px;align-items:center;font-size:14px;color:var(--sky);font-weight:500}
.top-contact span{display:flex;align-items:center;gap:10px}
.icon-box{width:32px;height:30px;border:2px solid var(--blue);display:flex;align-items:center;justify-content:center}
.main-nav{right:112px;top:80px;display:flex;gap:54px;font-size:14px;font-weight:600;color:var(--ink)}

/* hero */
.hero{left:0;top:120px;width:1200px;height:618px;background:linear-gradient(120deg,#6b5a4a 0%,#4f6c8c 40%,#8a8b84 70%,#5a5048 100%)}
.hero-cut{left:0;top:650px}
.hero-name{left:111px;top:244px;font-size:70px;font-weight:700;color:var(--white);line-height:1.1}
.hero-text{left:111px;top:362px;width:500px;font-size:17px;line-height:1.75;color:var(--white)}
.btn-outline{left:111px;top:452px;width:126px;height:53px;border:2px solid var(--white);color:var(--white);font-size:17px;display:flex;align-items:center;justify-content:center}
.dots{left:553px;top:702px;display:flex;gap:5px}
.dots i{width:14px;height:14px;border-radius:50%;background:#7fc4ec;display:block}
.dots i:first-child{background:var(--blue)}

/* section titles */
.section-title{border:3px solid var(--blue);color:var(--blue);font-weight:800;font-size:33px;padding:4px 15px;line-height:1.35;white-space:nowrap}
.section-title.light{border-color:var(--white);color:var(--white)}

/* services */
.service{width:230px;height:230px;border-radius:50%;border:7px solid var(--blue);padding:8px}
.service.alt{border-color:var(--sky)}
.service-photo{width:100%;height:100%;border-radius:50%;background:radial-gradient(circle at 40% 35%,#4d9ad8,#1c5ea7);display:flex;flex-direction:column;align-items:center;justify-content:center;color:var(--white);font-size:16px;font-weight:600;text-align:center;line-height:1.4;gap:10px}
.service.alt .service-photo{background:radial-gradient(circle at 40% 35%,#5ab8ea,#1d87cb)}
.arrow{top:1024px}

/* about */
.about{left:0;top:1262px;width:1200px;height:658px;background:var(--grey-bg)}
.about-lead{left:111px;top:1426px;width:530px;font-size:15.5px;line-height:1.7;color:var(--blue);font-weight:500}
.about-body{left:111px;width:527px;font-size:13.5px;line-height:1.95;text-align:justify;color:#444}
.btn-blue{left:111px;top:1753px;width:125px;height:44px;border:3px solid var(--blue);border-top:none;border-right:none;color:var(--blue);font-size:18px;font-weight:600;display:flex;align-items:center;justify-content:center}
.btn-blue::before{content:"";position:absolute;right:-3px;top:0;width:3px;height:10px;background:var(--blue)}
.btn-blue::after{content:"";position:absolute;left:0;top:0;width:100%;height:3px;background:var(--blue)}
.about-frame{left:718px;top:1373px;width:344px;height:462px;border:7px solid var(--sky)}
.about-photo{left:744px;top:1347px;width:344px;height:462px;background:linear-gradient(160deg,#a8acad 0%,#cfcfc8 40%,#7d7461 75%,#c7a03a 100%)}

/* banners */
.banner{top:1920px;width:600px;height:428px;color:var(--white)}
.banner-left{left:0;background:linear-gradient(180deg,#2d98d8 0%,#1f7ec6 60%,#2a6eaa 100%)}
.banner-right{left:600px;background:linear-gradient(160deg,#4b5868 0%,#3d4655 50%,#5b5e60 100%)}
.banner-small{font-size:24px;font-weight:500}
.banner-big{font-size:35px;font-weight:800;margin-top:4px}
.banner-text{font-size:13.5px;line-height:1.8;margin-top:12px;width:460px}

/* news */
.news-card{top:2568px;width:308px;text-align:center}
.news-photo{width:308px;height:200px;clip-path:polygon(0 0,100% 0,100% 100%,50% 88%,0 100%)}
.news-date{margin-top:28px;font-size:15px;color:var(--blue);display:flex;justify-content:center;align-items:center;gap:6px}
.news-title{margin-top:16px;font-size:14.5px;line-height:1.75;color:#333;font-weight:500}
.news-rule{width:102px;height:5px;background:var(--sky);margin:24px auto 0}

/* achievements */
.achieve{left:0;top:3000px;width:1200px;height:540px;background:linear-gradient(90deg,#2a3a36 0%,#3a3f46 30%,#4d5056 50%,#3a3f46 70%,#2d3a3a 100%)}
.stat{top:3260px;height:82px;border:3px solid var(--white);border-right:none;display:flex;align-items:center;gap:14px;padding-left:16px;color:var(--white)}
.stat::after{content:"";position:absolute;right:0;top:-3px;width:3px;height:12px;background:var(--white)}
.stat-num{font-size:29px;font-weight:700;line-height:1}
.stat-label{font-size:18px;font-weight:600;margin-top:4px}

/* footer */
.footer-about{left:111px;top:3720px;width:364px;font-size:14.5px;line-height:1.6;text-align:justify;color:#555}
.footer-head{font-size:21px;font-weight:700;color:var(--sky)}
.quick-links{left:577px;top:3633px}
.quick-links ul{list-style:none;margin-top:16px;font-size:15px;line-height:1.6;color:#444}
.quick-links li{display:flex;align-items:center;gap:10px}
.contact-info{left:838px;top:3633px;width:260px}
.contact-info ul{list-style:none;margin-top:16px;font-size:14.5px;line-height:1.65;color:#444}
.contact-info li{display:flex;gap:10px;margin-bottom:10px}
.footer-rule{left:111px;top:3868px;width:977px;height:1px;background:#bbb}
.copyright{left:0;top:3898px;width:1200px;text-align:center;font-size:15px;color:#444}
</style>
</head>
<body>

<header class="site-header abs">
  <div class="brand abs"><span class="brand-name">VORNAK</span></div>
  <div class="top-contact abs">
    <span><span class="icon-box"><svg width="16" height="16" viewBox="0 0 24 24"><path d="M6.6 10.8a15 15 0 006.6 6.6l2.2-2.2a1 1 0 011-.25 11 11 0 003.5.56 1 1 0 011 1V20a1 1 0 01-1 1A17 17 0 013 4a1 1 0 011-1h3.5a1 1 0 011 1 11 11 0 00.56 3.5 1 1 0 01-.25 1z" fill="none" stroke="#1a6cbd" stroke-width="1.8"/></svg></span>+27 (0) 11 555 0192</span>
    <span><span class="icon-box"><svg width="18" height="14" viewBox="0 0 24 18"><rect x="1" y="1" width="22" height="16" fill="none" stroke="#1a6cbd" stroke-width="2"/><path d="M1 1l11 9 11-9" fill="none" stroke="#1a6cbd" stroke-width="2"/></svg></span>hello@vornak.co.za</span>
  </div>
  <nav class="main-nav abs"><a>HOME</a><a>ABOUT</a><a>SERVICES</a><a>NEWS</a><a>CONTACT</a></nav>
</header>

<section class="hero abs" role="img" aria-label="Two construction workers in hard hats reviewing plans on site"></section>
<svg class="hero-cut abs" width="1200" height="90" viewBox="0 0 1200 90"><polygon points="0,88 600,10 1200,88 1200,90 0,90" fill="#fff"/></svg>
<div class="hero-name abs">VORNAK</div>
<p class="hero-text abs">Duis aute irure dolor in reprehenderit in voluptate velit esse cillum dolore eu fugiat nulla pariatur.</p>
<a class="btn-outline abs">Read More</a>
<div class="dots abs"><i></i><i></i><i></i><i></i><i></i></div>

<h2 class="section-title abs" style="left:464px;top:792px">OUR SERVICES</h2>
<svg class="arrow abs" style="left:46px" width="24" height="44" viewBox="0 0 24 44"><path d="M22 2L2 22l20 20" fill="none" stroke="#555" stroke-width="2"/></svg>
<svg class="arrow abs" style="left:1130px" width="24" height="44" viewBox="0 0 24 44"><path d="M2 2l20 20L2 42" fill="none" stroke="#555" stroke-width="2"/></svg>

<div class="service abs" style="left:111px;top:927px"><div class="service-photo" role="img" aria-label="Construction site in blue tone">
  <svg width="48" height="48" viewBox="0 0 48 48"><path d="M8 30a16 16 0 0132 0zM4 30h40v5H4z" fill="#fff"/><circle cx="24" cy="38" r="6" fill="none" stroke="#fff" stroke-width="3"/></svg>CONSTRUCTION</div></div>
<div class="service alt abs" style="left:359px;top:927px"><div class="service-photo" role="img" aria-label="Modern building in blue tone">
  <svg width="46" height="50" viewBox="0 0 46 50"><rect x="6" y="3" width="26" height="36" fill="none" stroke="#fff" stroke-width="3"/><path d="M12 12h14M12 19h14" stroke="#fff" stroke-width="3"/><path d="M24 48V36l10-8 10 8v12z" fill="#fff"/></svg>PROPERTY<br>DEVELOPMENT</div></div>
<div class="service abs" style="left:607px;top:927px"><div class="service-photo" role="img" aria-label="Mining vehicle in blue tone">
  <svg width="56" height="44" viewBox="0 0 56 44"><path d="M4 8h48l-6 20H10z" fill="none" stroke="#fff" stroke-width="3.5"/><circle cx="16" cy="36" r="5" fill="none" stroke="#fff" stroke-width="3"/><circle cx="40" cy="36" r="5" fill="none" stroke="#fff" stroke-width="3"/></svg>MINING</div></div>
<div class="service alt abs" style="left:855px;top:927px"><div class="service-photo" role="img" aria-label="Truck on road in blue tone">
  <svg width="60" height="44" viewBox="0 0 60 44"><rect x="3" y="4" width="34" height="26" fill="none" stroke="#fff" stroke-width="3"/><path d="M37 12h12l8 10v8H37z" fill="none" stroke="#fff" stroke-width="3"/><circle cx="14" cy="36" r="5" fill="#fff"/><circle cx="46" cy="36" r="5" fill="#fff"/></svg>TRANSPORT</div></div>

<section class="about abs"></section>
<h2 class="section-title abs" style="left:111px;top:1343px">ABOUT VORNAK</h2>
<p class="about-lead abs">Nam varius iaculis porttitor. Ut ac pharetra nulla, nec dictum nibh. Suspendisse the sodales quis enim ac ornare.</p>
<p class="about-body abs" style="top:1492px">Nam varius iaculis porttitor. Ut ac pharetra nulla, nec dictum nibh. Sus pen disse the sodales quis enim ac ornare. Sed id lacus volutpat, im perdiet quam a, fermentum mi. Etiam urna sapien, tempor in accumsan eu, consequat sed neque. Nam varius iaculis porttitor.</p>
<p class="about-body abs" style="top:1612px">Iaculis porttitor. Ut ac pharetra nulla, nec dictum nibh. Sus pen disse the sodales quis enim ac ornare. Sed id lacus volutpat, im perdiet quam a, fer mentum mi. Etiam urna sapien, tempor in accumsan eu, consequat sed neque. Nam varius iaculis porttitor.</p>
<a class="btn-blue abs">Read More</a>
<div class="about-frame abs"></div>
<div class="about-photo abs" role="img" aria-label="Construction worker in hard hat holding a shovel at a building site"></div>

<section class="banner banner-left abs" role="img" aria-label="Large mining dump truck with blue overlay">
  <div class="abs" style="left:111px;top:230px">
    <div class="banner-small">Vornak is Ready to</div>
    <div class="banner-big">BUILD YOUR DREAM</div>
    <p class="banner-text">Proin lorem nulla, imperdiet sit amet diam id, mollis varius orci. In iaculis mi eu ipsum feugiat volutpat.</p>
  </div>
</section>
<section class="banner banner-right abs" role="img" aria-label="Engineers in hard hats reviewing plans near cranes">
  <div class="abs" style="left:40px;top:230px">
    <div class="banner-small">Vornak is Leader of</div>
    <div class="banner-big">CONSTRUCTION</div>
    <p class="banner-text">Proin lorem nulla, imperdiet sit amet diam id, mollis varius orci. In iaculis mi eu ipsum feugiat volutpat.</p>
  </div>
</section>

<h2 class="section-title abs" style="left:437px;top:2433px">COMPANY NEWS</h2>

<article class="news-card abs" style="left:111px">
  <div class="news-photo" role="img" aria-label="Person working on a laptop at a desk" style="background:linear-gradient(120deg,#e8e6e2,#9a9aa0 60%,#4c4c52)"></div>
  <div class="news-date"><svg width="14" height="14" viewBox="0 0 14 14"><circle cx="7" cy="7" r="6" fill="none" stroke="#1a6cbd" stroke-width="1.5"/><path d="M4 7l2 2 4-4" fill="none" stroke="#1a6cbd" stroke-width="1.5"/></svg>April 1, 2018</div>
  <p class="news-title">NEMO ENIM IPSAM VOLUPTATEM QUIA VOLUPTAS SIT ASPERNATUR</p>
  <div class="news-rule"></div>
</article>
<article class="news-card abs" style="left:447px">
  <div class="news-photo" role="img" aria-label="Yellow mining truck on a gravel site" style="background:linear-gradient(180deg,#8fa6bd 0%,#c9b07a 55%,#4f4a44 100%)"></div>
  <div class="news-date"><svg width="14" height="14" viewBox="0 0 14 14"><circle cx="7" cy="7" r="6" fill="none" stroke="#1a6cbd" stroke-width="1.5"/><path d="M4 7l2 2 4-4" fill="none" stroke="#1a6cbd" stroke-width="1.5"/></svg>April 1, 2018</div>
  <p class="news-title">NEMO ENIM IPSAM VOLUPTATEM QUIA VOLUPTAS SIT ASPERNATUR</p>
  <div class="news-rule"></div>
</article>
<article class="news-card abs" style="left:781px">
  <div class="news-photo" role="img" aria-label="Red truck cab at sunset" style="background:linear-gradient(110deg,#2a3344 0%,#8a3a28 50%,#d59a55 100%)"></div>
  <div class="news-date"><svg width="14" height="14" viewBox="0 0 14 14"><circle cx="7" cy="7" r="6" fill="none" stroke="#1a6cbd" stroke-width="1.5"/><path d="M4 7l2 2 4-4" fill="none" stroke="#1a6cbd" stroke-width="1.5"/></svg>April 1, 2018</div>
  <p class="news-title">NEMO ENIM IPSAM VOLUPTATEM QUIA VOLUPTAS SIT ASPERNATUR</p>
  <div class="news-rule"></div>
</article>

<section class="achieve abs" role="img" aria-label="Delivery van driving on a blurred road"></section>
<svg class="abs" style="left:0;top:3430px" width="1200" height="113" viewBox="0 0 1200 113">
  <polygon points="0,20 600,100 1200,20 1200,113 0,113" fill="#fff"/>
  <polyline points="0,6 600,86 1200,6" fill="none" stroke="#1a6cbd" stroke-width="6"/>
  <polyline points="0,22 600,102 1200,22" fill="none" stroke="#1a6cbd" stroke-width="5"/>
</svg>
<h2 class="section-title light abs" style="left:412px;top:3085px">OUR ACHIEVEMENT</h2>

<div class="stat abs" style="left:111px;width:194px">
  <svg width="40" height="44" viewBox="0 0 40 44"><path d="M10 4h20v12a10 10 0 01-20 0zM10 8H3v4a7 7 0 007 7M30 8h7v4a7 7 0 01-7 7M20 26v8M12 40h16v-6H12z" fill="none" stroke="#fff" stroke-width="2"/></svg>
  <div><div class="stat-num">4905</div><div class="stat-label">Awards Won</div></div>
</div>
<div class="stat abs" style="left:340px;width:200px">
  <svg width="36" height="44" viewBox="0 0 36 44"><rect x="8" y="2" width="26" height="34" fill="none" stroke="#fff" stroke-width="2"/><rect x="2" y="8" width="26" height="34" fill="#3a3f46" stroke="#fff" stroke-width="2"/><path d="M7 17h16M7 23h16M7 29h16M7 35h10" stroke="#fff" stroke-width="2"/></svg>
  <div><div class="stat-num">3750</div><div class="stat-label">Total Projects</div></div>
</div>
<div class="stat abs" style="left:577px;width:256px">
  <svg width="36" height="44" viewBox="0 0 36 44"><rect x="3" y="3" width="28" height="38" rx="2" fill="none" stroke="#fff" stroke-width="2"/><path d="M9 14h16M9 21h16M9 28h10" stroke="#fff" stroke-width="2"/><path d="M20 34l4 4 8-10" fill="none" stroke="#fff" stroke-width="2"/></svg>
  <div><div class="stat-num">4782</div><div class="stat-label">Completed Projects</div></div>
</div>
<div class="stat abs" style="left:866px;width:222px">
  <svg width="40" height="40" viewBox="0 0 40 40"><circle cx="24" cy="12" r="7" fill="none" stroke="#fff" stroke-width="2"/><path d="M10 36a14 14 0 0128 0z" fill="none" stroke="#fff" stroke-width="2"/><circle cx="10" cy="18" r="5" fill="none" stroke="#fff" stroke-width="2"/><path d="M2 36a9 9 0 0110-10" fill="none" stroke="#fff" stroke-width="2"/></svg>
  <div><div class="stat-num">3237</div><div class="stat-label">Satisfied Clients</div></div>
</div>

<footer>
  <div class="brand abs" style="top:3630px"><span class="brand-name">VORNAK</span></div>
  <p class="footer-about abs">Nemo enim ipsam voluptatem quia voluptas sit aspernatur aut odit aut fugit, sed quia consequuntur magni dolores eos qui rationes.</p>
  <div class="quick-links abs">
    <h3 class="footer-head">Quick Links</h3>
    <ul>
      <li><svg width="14" height="12" viewBox="0 0 14 12"><path d="M1 6h9M7 2l4 4-4 4" fill="none" stroke="#1a6cbd" stroke-width="1.6"/></svg>Home</li>
      <li><svg width="14" height="12" viewBox="0 0 14 12"><path d="M1 6h9M7 2l4 4-4 4" fill="none" stroke="#1a6cbd" stroke-width="1.6"/></svg>About</li>
      <li><svg width="14" height="12" viewBox="0 0 14 12"><path d="M1 6h9M7 2l4 4-4 4" fill="none" stroke="#1a6cbd" stroke-width="1.6"/></svg>Services</li>
      <li><svg width="14" height="12" viewBox="0 0 14 12"><path d="M1 6h9M7 2l4 4-4 4" fill="none" stroke="#1a6cbd" stroke-width="1.6"/></svg>Projects</li>
      <li><svg width="14" height="12" viewBox="0 0 14 12"><path d="M1 6h9M7 2l4 4-4 4" fill="none" stroke="#1a6cbd" stroke-width="1.6"/></svg>News</li>
      <li><svg width="14" height="12" viewBox="0 0 14 12"><path d="M1 6h9M7 2l4 4-4 4" fill="none" stroke="#1a6cbd" stroke-width="1.6"/></svg>Contact Us</li>
    </ul>
  </div>
  <div class="contact-info abs">
    <h3 class="footer-head">Contact Information</h3>
    <ul>
      <li><svg width="16" height="20" viewBox="0 0 16 20" style="flex:none"><path d="M8 19s6-6.5 6-11A6 6 0 002 8c0 4.5 6 11 6 11z" fill="none" stroke="#1a6cbd" stroke-width="1.6"/><circle cx="8" cy="8" r="2" fill="none" stroke="#1a6cbd" stroke-width="1.6"/></svg>Nemo enim ipsam voluptatem quia voluptasem</li>
      <li><svg width="16" height="16" viewBox="0 0 24 24" style="flex:none"><path d="M6.6 10.8a15 15 0 006.6 6.6l2.2-2.2a1 1 0 011-.25 11 11 0 003.5.56 1 1 0 011 1V20a1 1 0 01-1 1A17 17 0 013 4a1 1 0 011-1h3.5a1 1 0 011 1 11 11 0 00.56 3.5 1 1 0 01-.25 1z" fill="none" stroke="#1a6cbd" stroke-width="2"/></svg>Phone: +27 (0) 11 555 0192</li>
      <li><svg width="16" height="14" viewBox="0 0 24 18" style="flex:none;margin-top:4px"><rect x="1" y="1" width="22" height="16" fill="none" stroke="#1a6cbd" stroke-width="2"/><path d="M1 1l11 9 11-9" fill="none" stroke="#1a6cbd" stroke-width="2"/></svg>Mail: hello@vornak.co.za</li>
    </ul>
  </div>
  <div class="footer-rule abs"></div>
  <p class="copyright abs">Copyrights @ 2018 Vornak. All Rights Reserved.</p>
</footer>

</body>
</html>
```